Software Specialist in Artificial Intelligence innovation needs a smart and professional looking bus

Prefers a clean and professional design, yet portraying a class of its own and a world-class feel. We develop state-of-the-art software automation engines by deploying artificial intelligence that simulates the smartest brains that are able to simulate a human consultant and/or data scientist. Both single-sided or double-sided design is acceptable. Do not refer too much to our current website as we are also in the process of revamping it so that it better reflects who we are and what we do.
Updates

Project Deadline Extended
Reason: A substantial number of designs submitted to date deviates a fair bit from requirements and expectations. Feedbacks will be provided to all parties by today and as such, an extension is catered to accomodate re-submissions.

Target Market(s)

Software technology companies, software developers, enterprise clients that requires automation supported by Artificial Intelligence driven software solutions.

Industry/Entity Type

Software

Contact Information for Business Card

Marlo Vance
Chief Innovator
marlovance@brightquill.example
mobile: +65 94417302
Company Name: BrightQuill Pte Ltd
Address: 14 Tessaly Road #03-11 Harrow Court, Singapore 539204
Telephone: +65 63175420
Website: www.BrightQuill.example
Please do not include the titles of the above fields.

Font styles to use
Sans Serif
Other font styles liked:
• Calibri, Futura Condensed

Requirements
Must have
• Portrays a professional and innovative image. Should reflect that the company is into Artificial Intelligence software development, high tech kind of feel.
Nice to have
• A plus point would be if you can even come up with a new company logo for us, representing who we are. Our current company logo is attached.
Should not have
• Fanciful stuffs as it must portray a professional image. Prefers not to have the cloud "image" as part of the logo or in the name card.

```html
<!DOCTYPE html>
<html lang="en">
<head>
<meta charset="utf-8">
<title>BrightQuill Business Card</title>
<link rel="stylesheet" href="https://fonts.googleapis.com/css2?family=Open+Sans:wght@400;600;700&display=swap">
<style>
  :root {
    --page-bg: #e9e6e1;
    --card-white: #ffffff;
    --card-black: #1b1b1c;
    --brand-red: #c23a4e;
    --ink-dark: #2b2b2b;
    --ink-grey: #6b6b6b;
    --band-blue: #2f86c6;
    --band-blue-deep: #1f5f9a;
    --tagline-grey: #d6d6d6;
    --accent-blue: #3f8fd6;
  }
  * { box-sizing: border-box; margin: 0; padding: 0; }
  html, body {
    width: 1200px; height: 1023px; overflow: hidden;
    background: var(--page-bg);
    font-family: "Open Sans", Arial, sans-serif;
  }
  .sheet { position: relative; width: 1200px; height: 1023px; }
  .card {
    position: absolute; width: 620px; height: 354px;
    border-radius: 4px; overflow: hidden;
    box-shadow: 0 10px 28px rgba(0,0,0,.22);
  }
  /* Front */
  .card-front { left: 120px; top: 110px; background: var(--card-white); }
  .brand {
    position: absolute; left: 36px; top: 46px;
    display: flex; align-items: center; gap: 12px;
  }
  .brand-dot {
    flex: none; width: 54px; height: 54px; border-radius: 50%;
    background: var(--accent-blue);
  }
  .brand-name {
    font-size: 32px; font-weight: 700; color: var(--brand-red); line-height: 1;
  }
  .brand-tagline {
    font-size: 11.5px; font-weight: 600; color: var(--ink-dark);
    margin-top: 6px; white-space: nowrap;
  }
  .company {
    position: absolute; left: 40px; top: 140px;
    font-size: 12.5px; color: var(--ink-grey); line-height: 1.6;
  }
  .company-name { color: var(--brand-red); margin-bottom: 2px; }
  .contact-row { display: flex; align-items: flex-start; gap: 8px; white-space: nowrap; }
  .icon { flex: none; width: 15px; height: 15px; margin-top: 3px; }
  .person { position: absolute; left: 372px; top: 46px; }
  .person-name {
    font-size: 22px; font-weight: 700; color: var(--brand-red); letter-spacing: .5px;
  }
  .person-title {
    font-size: 16px; font-weight: 600; color: var(--brand-red); margin-top: 2px;
  }
  .person-contacts {
    margin-top: 18px; font-size: 13px; color: var(--ink-dark); line-height: 1.8;
  }
  .card-band { position: absolute; left: 0; bottom: 0; width: 620px; height: 60px; }
  /* Back */
  .card-back { left: 460px; top: 540px; background: var(--card-black); }
  .back-text { position: absolute; left: 44px; top: 120px; }
  .back-name {
    font-size: 52px; font-weight: 700; color: #ffffff; line-height: 1;
  }
  .back-tagline {
    font-size: 14px; letter-spacing: 2.5px; color: var(--tagline-grey);
    margin-top: 14px; white-space: nowrap;
  }
  .back-dot {
    position: absolute; right: 44px; top: 117px;
    width: 120px; height: 120px; border-radius: 50%;
    background: var(--accent-blue);
  }
</style>
</head>
<body>
<main class="sheet">

  <section class="card card-front" aria-label="Business card front">
    <div class="brand">
      <span class="brand-dot"></span>
      <div>
        <div class="brand-name">BrightQuill</div>
        <div class="brand-tagline">Building the Intelligent Enterprise</div>
      </div>
    </div>

    <div class="company">
      <div class="company-name">BrightQuill Pte Ltd:</div>
      <div class="contact-row">
        <svg class="icon" viewBox="0 0 16 16"><rect width="16" height="16" rx="3" fill="var(--brand-red)"/><path d="M5 4h2l1 3-1.5 1a6 6 0 0 0 2.5 2.5L10 9l3 1v2a1 1 0 0 1-1 1A9 9 0 0 1 4 5a1 1 0 0 1 1-1z" fill="#fff"/></svg>
        <span>+65 63175420</span>
      </div>
      <div class="contact-row">
        <svg class="icon" viewBox="0 0 16 16"><rect width="16" height="16" rx="3" fill="var(--brand-red)"/><circle cx="8" cy="8" r="4.5" fill="none" stroke="#fff" stroke-width="1.2"/><path d="M3.5 8h9M8 3.5v9" stroke="#fff" stroke-width="1"/></svg>
        <span>www.BrightQuill.example</span>
      </div>
      <div class="contact-row">
        <svg class="icon" viewBox="0 0 16 16"><rect width="16" height="16" rx="3" fill="var(--brand-red)"/><path d="M8 3a3.2 3.2 0 0 1 3.2 3.2C11.2 9 8 13 8 13S4.8 9 4.8 6.2A3.2 3.2 0 0 1 8 3z" fill="#fff"/><circle cx="8" cy="6.2" r="1.2" fill="var(--brand-red)"/></svg>
        <span>14 Tessaly Road<br>#03-11 Harrow Court,<br>Singapore 539204</span>
      </div>
    </div>

    <div class="person">
      <div class="person-name">MARLO VANCE</div>
      <div class="person-title">Chief Innovator</div>
      <div class="person-contacts">
        <div class="contact-row">
          <svg class="icon" viewBox="0 0 16 16"><rect width="16" height="16" rx="3" fill="var(--brand-red)"/><rect x="5" y="2.5" width="6" height="11" rx="1" fill="#fff"/><rect x="6" y="4" width="4" height="7" fill="var(--brand-red)"/></svg>
          <span>+65 94417302</span>
        </div>
        <div class="contact-row">
          <svg class="icon" viewBox="0 0 16 16"><rect width="16" height="16" rx="3" fill="var(--brand-red)"/><rect x="3" y="4.5" width="10" height="7" fill="#fff"/><path d="M3 4.5l5 4 5-4" fill="none" stroke="var(--brand-red)" stroke-width="1"/></svg>
          <span>marlovance@brightquill.example</span>
        </div>
      </div>
    </div>

    <svg class="card-band" viewBox="0 0 620 60" preserveAspectRatio="none" aria-hidden="true">
      <defs>
        <linearGradient id="bandBlue" x1="0" y1="0" x2="0" y2="1">
          <stop offset="0" stop-color="var(--band-blue)"/>
          <stop offset="1" stop-color="var(--band-blue-deep)"/>
        </linearGradient>
      </defs>
      <polygon points="0,34 300,34 318,22 620,22 620,60 0,60" fill="url(#bandBlue)"/>
      <polygon points="300,26 316,14 620,14 620,20 318,20 302,32" fill="var(--brand-red)"/>
    </svg>
  </section>

  <section class="card card-back" aria-label="Business card back">
    <div class="back-text">
      <div class="back-name">BrightQuill</div>
      <div class="back-tagline">Building the Intelligent Enterprise</div>
    </div>
    <span class="back-dot"></span>
  </section>

</main>
</body>
</html>
```